Harbinger Crude Advisors needs a logo design and business card layout.

HCA is a consulting firm in oil and gas, specializing in upstream engineering and field work. We provide engineering solutions for the complete wellbore cycle from casing design to flowback. This includes completion and production design. On-site job supervision and project engineering for conventional and unconventional reservoirs. Asset analysis by reviewing operational conditions of asset packages to determine value of potential acquisitions or divesture.

```html
<!DOCTYPE html>
<html lang="en">
<head>
<meta charset="utf-8">
<title>Harbinger Crude Advisors – Logo and Business Card</title>
<link rel="stylesheet" href="https://fonts.googleapis.com/css2?family=Raleway:wght@400;500;600&family=Lato:wght@400&display=swap">
<style>
  :root {
    --stage: #161616;
    --card-dark: #2a2526;
    --card-light: #f4f4f2;
    --gold: #f2b51c;
    --gold-deep: #d99e0e;
    --ink: #1d1d1d;
    --ink-soft: #3a3a3a;
    --white: #ffffff;
  }
  * { box-sizing: border-box; margin: 0; padding: 0; }
  html, body { width: 1200px; height: 900px; overflow: hidden; }
  body {
    background: var(--stage);
    font-family: "Raleway", sans-serif;
    position: relative;
  }
  .card {
    position: absolute;
    width: 520px;
    height: 298px;
    border-radius: 22px;
    overflow: hidden;
    box-shadow: 0 14px 30px rgba(0,0,0,.55);
  }
  /* front */
  .card--front {
    left: 150px; top: 80px;
    background: var(--card-dark);
    display: flex; flex-direction: column; align-items: center; justify-content: center;
  }
  .brand-mark {
    font-family: "Raleway", sans-serif;
    font-weight: 500;
    letter-spacing: 2px;
    line-height: 1;
  }
  .brand-name {
    font-family: "Raleway", sans-serif;
    font-weight: 500;
    line-height: 1;
    white-space: nowrap;
  }
  .card--front .brand-mark { font-size: 58px; color: var(--gold); margin-bottom: 14px; }
  .card--front .brand-name { font-size: 30px; color: var(--white); }

  /* back */
  .card--back {
    left: 560px; top: 430px;
    background: var(--card-light);
  }
  .back-logo {
    position: absolute; left: 28px; top: 92px; width: 250px;
    display: flex; flex-direction: column; align-items: center;
  }
  .card--back .brand-mark { font-size: 44px; color: var(--gold); margin-bottom: 10px; }
  .card--back .brand-name { font-size: 21px; color: var(--ink); }
  .back-divider {
    position: absolute; left: 292px; top: 42px;
    width: 1.5px; height: 142px; background: var(--gold);
  }
  .contact {
    position: absolute; left: 316px; top: 48px;
    font-family: "Lato", sans-serif; color: var(--ink);
  }
  .contact__name { font-family: "Raleway", sans-serif; font-weight: 500; font-size: 21px; }
  .contact__title { font-size: 13px; color: var(--gold-deep); margin-top: 2px; }
  .contact__list { list-style: none; margin-top: 18px; font-size: 13px; }
  .contact__list li { display: flex; align-items: center; gap: 8px; margin-bottom: 6px; }
  .contact__list svg { width: 13px; height: 13px; flex: none; }
  .back-band {
    position: absolute; left: 0; right: 0; bottom: 0; height: 78px;
    background: linear-gradient(90deg, var(--gold-deep), var(--gold) 55%, var(--gold-deep));
    border-top: 4px solid var(--ink);
    display: flex; align-items: center; justify-content: center;
  }
  .back-band__web {
    font-family: "Lato", sans-serif; font-size: 14px; letter-spacing: 3px; color: var(--ink-soft);
  }

  /* logo lockup */
  .lockup {
    position: absolute; left: 40px; top: 650px; width: 440px;
    display: flex; flex-direction: column; align-items: center;
  }
  .lockup .brand-mark { font-size: 80px; color: var(--gold); margin-bottom: 26px; }
  .lockup .brand-name { font-size: 38px; color: var(--white); }
</style>
</head>
<body>
  <section class="card card--front" aria-label="Business card front">
    <div class="brand-mark">HCA</div>
    <div class="brand-name">Harbinger Crude Advisors</div>
  </section>

  <section class="card card--back" aria-label="Business card back">
    <div class="back-logo">
      <div class="brand-mark">HCA</div>
      <div class="brand-name">Harbinger Crude Advisors</div>
    </div>
    <div class="back-divider"></div>
    <div class="contact">
      <div class="contact__name">Your Name</div>
      <div class="contact__title">Job Title</div>
      <ul class="contact__list">
        <li>
          <svg viewBox="0 0 16 16" aria-hidden="true"><path fill="#f2b51c" d="M3 2h3l1.5 3.5-2 1.2a8 8 0 0 0 3.8 3.8l1.2-2L14 10v3a1 1 0 0 1-1 1A12 12 0 0 1 2 3a1 1 0 0 1 1-1z"/></svg>
          000 000 0000
        </li>
        <li>
          <svg viewBox="0 0 16 16" aria-hidden="true"><rect x="1" y="3" width="14" height="10" rx="1" fill="#f2b51c"/><path d="M1.5 3.8 8 9l6.5-5.2" stroke="#fff" stroke-width="1.3" fill="none"/></svg>
          yourname@hcadvisors.com
        </li>
      </ul>
    </div>
    <div class="back-band">
      <span class="back-band__web">www.hcadvisors.com</span>
    </div>
  </section>

  <section class="lockup" aria-label="Logo lockup">
    <div class="brand-mark">HCA</div>
    <div class="brand-name">Harbinger Crude Advisors</div>
  </section>
</body>
</html>
```